MOLVT Study flyer

I need help designing a flyer for a research study that will include brain imaging in adolescents. The info is in the attached document. The study is called the Marrowby Orchard Lantern Vesper Trail (MOLVT) study. Ideally this would be returned as a document that I can edit in the future as we will have several new recruitment phases (different age groups, etc. I also would love to have a logo designed as part of this project, but I recognize that might be a separate design request.

```html
<!DOCTYPE html>
<html lang="en">
<head>
<meta charset="utf-8">
<title>MOLVT Study flyer</title>
<link rel="stylesheet" href="https://fonts.googleapis.com/css2?family=Barlow+Condensed:wght@400;500;600&display=swap">
<style>
  :root {
    --page: #e6e6e6;
    --navy-deep: #0a111f;
    --navy: #0f1c33;
    --blue-glow: #1d4f9c;
    --blue-soft: #123a78;
    --cyan: #4fd8ef;
    --cyan-soft: #8fe6f5;
    --text: #ffffff;
  }
  * { margin: 0; padding: 0; box-sizing: border-box; }
  html, body { width: 1200px; height: 1200px; overflow: hidden; }
  body {
    background: var(--page);
    font-family: "Barlow Condensed", "Arial Narrow", sans-serif;
    color: var(--text);
    position: relative;
  }
  .flyer {
    position: absolute;
    left: 221px; top: 65px;
    width: 756px; height: 1070px;
    background: radial-gradient(ellipse at 30% 20%, var(--navy) 0%, var(--navy-deep) 75%);
    overflow: hidden;
  }
  .backdrop { position: absolute; inset: 0; width: 100%; height: 100%; }
  .brain-art {
    position: absolute;
    left: 98px; top: 41px; width: 562px; height: 306px;
    border-radius: 48% 52% 40% 46% / 58% 58% 42% 42%;
    border: 2px solid rgba(79,216,239,0.55);
    box-shadow: 0 0 28px rgba(79,216,239,0.35), inset 0 0 40px rgba(79,216,239,0.25);
    background: radial-gradient(ellipse at 50% 45%, rgba(79,216,239,0.28) 0%, rgba(29,79,156,0.3) 55%, rgba(15,28,51,0.2) 100%);
  }
  .headline {
    position: absolute; left: 0; right: 0; top: 312px;
    text-align: center; font-weight: 600; font-size: 36px; line-height: 50px;
  }
  .intro {
    position: absolute; left: 44px; top: 453px; width: 680px;
    font-size: 17px; line-height: 25px; font-weight: 400;
  }
  .payment {
    position: absolute; right: 40px; top: 506px;
    font-size: 30px; font-weight: 600; color: var(--cyan-soft);
  }
  .section-title {
    position: absolute; left: 44px;
    font-size: 21px; font-weight: 600;
  }
  .section-title.involves { top: 591px; }
  .section-title.eligible { top: 765px; }
  .detail-list {
    position: absolute; left: 44px; width: 670px;
    list-style: none; font-size: 17px; line-height: 25px; font-weight: 400;
  }
  .detail-list.involves { top: 643px; }
  .detail-list.eligible { top: 817px; }
  .detail-list li { position: relative; padding-left: 29px; }
  .detail-list li::before { content: "-"; position: absolute; left: 2px; }
  .cta {
    position: absolute; left: 0; right: 0; top: 940px;
    text-align: center; font-size: 21px; font-weight: 600;
  }
  .contact {
    position: absolute; left: 0; right: 0; top: 988px;
    text-align: center; font-size: 17px; font-weight: 400;
  }
</style>
</head>
<body>
  <main class="flyer">
    <svg class="backdrop" viewBox="0 0 756 1070" aria-hidden="true">
      <defs>
        <radialGradient id="orb-left" cx="50%" cy="50%" r="50%">
          <stop offset="0%" stop-color="#1d4f9c" stop-opacity="0.55"/>
          <stop offset="100%" stop-color="#123a78" stop-opacity="0.2"/>
        </radialGradient>
        <radialGradient id="orb-right" cx="40%" cy="40%" r="60%">
          <stop offset="0%" stop-color="#1d5aa8" stop-opacity="0.5"/>
          <stop offset="100%" stop-color="#0a111f" stop-opacity="0"/>
        </radialGradient>
      </defs>
      <circle cx="120" cy="600" r="330" fill="url(#orb-left)"/>
      <circle cx="560" cy="830" r="330" fill="url(#orb-right)"/>
      <circle cx="400" cy="230" r="360" fill="none" stroke="#2a7fc0" stroke-opacity="0.4" stroke-width="2"/>
    </svg>

    <div class="brain-art" role="img" aria-label="Glowing line illustration of a human brain with connected neuron points"></div>

    <h1 class="headline">Are you the parent of a child age 10-17?<br>Do they worry or overthink negative emotions?</h1>

    <p class="intro">Halvern State University researchers are seeking girls age 10-17 for a study about brain activity in emotions and decision-making and how they relate to puberty, anxiety and depression</p>

    <p class="payment">up to $140</p>

    <h2 class="section-title involves">Study participation involves:</h2>
    <ul class="detail-list involves">
      <li>One one-hour interview (online or in-person) where your child will discuss their thoughts</li>
      <li>Online questionnaires (parent and child)</li>
      <li>One two-hour visit where your child will complete an MRI scan, answer questions about their puberty stage, and have a small hair sample taken to study puberty hormones</li>
    </ul>

    <h2 class="section-title eligible">Your child may be eligible if they:</h2>
    <ul class="detail-list eligible">
      <li>Are age 10-17</li>
      <li>Tend to worry or overthink negative thoughts</li>
      <li>have not been diagnosed with psychosis, learning problems, or autism</li>
    </ul>

    <p class="cta">Interested in participating? Want more information? Please contact us!</p>
    <p class="contact">molvtstudy@halvernhealth.edu</p>
  </main>
</body>
</html>
```